Contactlens Order Service - Redesign of Prototype

I've created a prototype for a contact and order service, but I'm a developer and not a designer. What I need is a redesign of the existing prototype. You should concentrate your efforts on two views: The Welcome View, that is a step-by-step for new users and the user page. Https://optiqra-dev.hostplain.com/ Welcome View: https://optiqra-dev.hostplain.com/welcome (only visible when you are not logged in.) You can find a working version of the prototype here: https://optiqra-dev.hostplain.com/ ) User: https://optiqra-dev.hostplain.com/user (you need to login, no panic - I delete the user account of the prototype every 5 days) Some general conditions: - I consider the logo as fixed - I used the material design framework: https://tessary.dev/build/web/ - It is a lot easier for me to use these components in your layouts too. - The Website is in English, I hope you know what things mean, google translate is your friend. - I expect every layout in Desktop AND mobile - it should be clear how things are displayed on smaller screens.
Updates
Hi! Just to clarify: I'm not looking for a complete new layout. I'm looking for a design that changes less, but makes the design look more professional. Please really take a look at the tessarys.dev website. best, Tobin
Target Market(s)
germany
Industry/Entity Type
Healthcare
Number of Pages Required
2 page
Font styles to use
Colors
Designer to choose colors to be used in the design.
Look and feel
Each slider illustrates characteristics of the customer's brand and the style your logo design should communicate.

```html
<!DOCTYPE html>
<html lang="de">
<head>
<meta charset="utf-8">
<title>Optiqra – Bestellung</title>
<link href="https://fonts.googleapis.com/css2?family=Roboto:wght@400;500;700;900&display=swap" rel="stylesheet">
<style>
:root{
  --stage:#0f1d3a;
  --brand:#1a56b8;
  --brand-dark:#134293;
  --page:#eef0f5;
  --card:#ffffff;
  --line:#dfe3ea;
  --muted:#8a93a3;
  --ink:#2b3340;
  --grey-btn:#8c929c;
  --step-off:#c9ced8;
  --photo:#d9e4ee;
}
*{box-sizing:border-box;margin:0;padding:0}
html,body{width:843px;height:1200px;overflow:hidden}
body{background:var(--stage);font-family:"Roboto",sans-serif;color:var(--ink);position:relative}
.screen{position:absolute;left:62px;width:719px;background:var(--page);overflow:hidden}
.screen--wizard{top:34px;height:514px}
.screen--overview{top:604px;height:562px}
.topbar{height:40px;background:var(--brand);display:flex;align-items:center;justify-content:space-between;padding:0 16px;color:#fff}
.topbar .left{display:flex;align-items:center;gap:14px}
.brand{font-weight:900;font-size:21px;letter-spacing:1px;color:#fff}
.footbar{position:absolute;left:0;right:0;bottom:0;height:26px;background:var(--brand);color:#cfe0ff;font-size:7px;display:flex;align-items:center;justify-content:center}
.footbar .ver{position:absolute;right:14px}
.white-band{background:#fff;height:110px;position:relative}
/* stepper */
.stepper{position:absolute;left:70px;right:70px;top:22px;height:60px}
.stepper .track{position:absolute;left:22px;right:22px;top:20px;height:3px;background:var(--step-off)}
.stepper .track span{display:block;width:33%;height:100%;background:var(--brand)}
.step{position:absolute;top:0;width:90px;margin-left:-45px;text-align:center}
.step .dot{width:42px;height:42px;border-radius:50%;margin:0 auto;background:#e4e7ed;display:flex;align-items:center;justify-content:center}
.step.active .dot{background:var(--brand)}
.step .label{font-size:7px;font-weight:500;color:var(--muted);margin-top:6px}
.step.active .label{color:var(--brand-dark)}
/* product card */
.product{position:absolute;left:58px;right:58px;top:142px;height:120px;background:var(--card);box-shadow:0 1px 4px rgba(0,0,0,.12);border-radius:3px}
.product .photo{position:absolute;left:18px;top:24px;width:118px;height:58px;background:linear-gradient(135deg,#e8eff6,var(--photo));border-radius:2px}
.product .info{position:absolute;left:156px;top:24px}
.product .type{font-size:8px;font-weight:700;color:var(--ink)}
.product .name{font-size:17px;font-weight:700;color:var(--brand);margin-top:2px}
.product .maker{font-size:7px;color:var(--muted);margin-top:2px}
.product .desc{font-size:7px;color:var(--muted);margin-top:10px}
.product .fields{position:absolute;right:52px;top:26px}
.field{display:flex;align-items:center;justify-content:flex-end;gap:8px;margin-bottom:8px;font-size:6.5px;color:var(--muted)}
.field .box{width:40px;height:14px;border:1px solid var(--line);font-size:6.5px;color:var(--ink);padding:3px 4px;display:flex;justify-content:space-between}
.product .trash{position:absolute;right:16px;top:12px}
.btn{position:absolute;top:360px;height:24px;width:58px;color:#fff;font-size:7px;font-weight:700;display:flex;align-items:center;justify-content:center;gap:5px;border-radius:2px}
.btn--back{left:58px;background:var(--grey-btn)}
.btn--next{right:58px;background:var(--brand)}
/* overview */
.title{text-align:center;color:var(--brand);font-size:19px;font-weight:700;margin-top:44px}
.summary{position:absolute;left:58px;right:58px;top:124px;background:var(--card);box-shadow:0 1px 4px rgba(0,0,0,.12);border-radius:3px}
.section-head{height:24px;display:flex;align-items:center;gap:8px;padding:0 14px;font-size:7px;font-weight:700;background:#f7f8fa;border-bottom:1px solid var(--line);color:var(--ink)}
.row{height:40px;display:flex;align-items:center;padding:0 14px;border-bottom:1px solid var(--line);position:relative}
.row .num{width:13px;height:13px;border-radius:50%;background:var(--brand);color:#fff;font-size:7px;font-weight:700;display:flex;align-items:center;justify-content:center;margin-right:10px}
.row .t{font-size:8px;font-weight:700;color:var(--brand)}
.row .s{font-size:7px;color:var(--muted);margin-top:2px}
.row .go{position:absolute;right:14px;width:15px;height:15px;border-radius:50%;background:#c5cad3;display:flex;align-items:center;justify-content:center}
.toggle{width:24px;height:10px;border-radius:5px;background:#c5cad3;position:relative;margin-right:12px}
.toggle::after{content:"";position:absolute;left:-2px;top:-2px;width:14px;height:14px;border-radius:50%;background:#fff;box-shadow:0 1px 2px rgba(0,0,0,.3)}
</style>
</head>
<body>

<svg width="0" height="0" style="position:absolute">
  <symbol id="menu" viewBox="0 0 16 14"><rect y="0" width="16" height="2.4" fill="#fff"/><rect y="5.8" width="16" height="2.4" fill="#fff"/><rect y="11.6" width="16" height="2.4" fill="#fff"/></symbol>
  <symbol id="user" viewBox="0 0 16 16"><circle cx="8" cy="5" r="3.6" fill="#fff"/><path d="M1 16c0-4 3-6.5 7-6.5s7 2.5 7 6.5z" fill="#fff"/></symbol>
  <symbol id="eye" viewBox="0 0 24 16"><path d="M1 8C4 3 8 1 12 1s8 2 11 7c-3 5-7 7-11 7S4 13 1 8z" fill="none" stroke="currentColor" stroke-width="2"/><circle cx="12" cy="8" r="3.5" fill="currentColor"/></symbol>
  <symbol id="truck" viewBox="0 0 24 16"><rect x="1" y="2" width="14" height="10" fill="currentColor"/><path d="M15 5h5l3 4v3h-8z" fill="currentColor"/><circle cx="6" cy="13.5" r="2" fill="#e4e7ed" stroke="currentColor" stroke-width="1.5"/><circle cx="19" cy="13.5" r="2" fill="#e4e7ed" stroke="currentColor" stroke-width="1.5"/></symbol>
  <symbol id="card" viewBox="0 0 24 16"><rect x="1" y="1" width="22" height="14" rx="2" fill="currentColor"/><rect x="1" y="4" width="22" height="3" fill="#e4e7ed"/></symbol>
  <symbol id="chev" viewBox="0 0 8 8"><path d="M3 1.5 5.5 4 3 6.5" fill="none" stroke="#fff" stroke-width="1.4"/></symbol>
</svg>

<section class="screen screen--wizard">
  <header class="topbar">
    <div class="left"><svg width="16" height="14"><use href="#menu"/></svg><span class="brand">OPTIQRA</span></div>
    <svg width="15" height="15"><use href="#user"/></svg>
  </header>
  <div class="white-band">
    <div class="stepper">
      <div class="track"><span></span></div>
      <div class="step active" style="left:0%"><div class="dot" style="color:#fff"><svg width="20" height="14"><use href="#eye"/></svg></div><div class="label">LINKES AUGE</div></div>
      <div class="step active" style="left:33.3%"><div class="dot" style="color:#fff"><svg width="20" height="14"><use href="#eye"/></svg></div><div class="label">RECHTES AUGE</div></div>
      <div class="step" style="left:66.6%"><div class="dot" style="color:#9aa2b0"><svg width="20" height="14"><use href="#truck"/></svg></div><div class="label">LIEFER- ADRESSE</div></div>
      <div class="step" style="left:100%"><div class="dot" style="color:#9aa2b0"><svg width="20" height="14"><use href="#card"/></svg></div><div class="label">BESTER PREIS</div></div>
    </div>
  </div>

  <article class="product">
    <div class="photo" role="img" aria-label="Produktfoto der Kontaktlinsen-Packung"></div>
    <div class="info">
      <div class="type">TAGESLINSEN</div>
      <div class="name">1 DAY CLARIVUE</div>
      <div class="maker">HALDEN &amp; ROWE</div>
      <div class="desc">Ihr tägliches Lieblingsprodukt</div>
    </div>
    <div class="fields">
      <div class="field">Packungsgröße<span class="box">30<span>▾</span></span></div>
      <div class="field">Stärke<span class="box">-3.0<span>▾</span></span></div>
      <div class="field">Achse<span class="box"><span></span><span>▾</span></span></div>
    </div>
    <svg class="trash" width="9" height="11" viewBox="0 0 9 11"><rect x="0" y="1" width="9" height="1.5" fill="#8a93a3"/><rect x="3" y="0" width="3" height="1.5" fill="#8a93a3"/><path d="M1 3h7l-.6 8H1.6z" fill="#8a93a3"/></svg>
  </article>

  <div class="btn btn--back">‹ BACK</div>
  <div class="btn btn--next">NEXT ›</div>

  <footer class="footbar">Copyright © 2017 All Rights Reserved<span class="ver">v0.1</span></footer>
</section>

<section class="screen screen--overview">
  <header class="topbar">
    <div class="left"><svg width="16" height="14"><use href="#menu"/></svg><span class="brand">OPTIQRA</span></div>
    <svg width="15" height="15"><use href="#user"/></svg>
  </header>
  <h1 class="title">Bitte Kontaklinsen auswählen!</h1>

  <div class="summary">
    <div class="section-head"><svg width="11" height="8" style="color:var(--ink)"><use href="#eye"/></svg>DEINE KONTAKTLINSEN</div>
    <div class="row"><span class="num">1</span><div><div class="t">LINKES AUGE</div><div class="s">Noch nicht gewählt</div></div><span class="go"><svg width="8" height="8"><use href="#chev"/></svg></span></div>
    <div class="row"><span class="num">2</span><div><div class="t">RECHTES AUGE</div><div class="s">Noch nicht gewählt</div></div><span class="go"><svg width="8" height="8"><use href="#chev"/></svg></span></div>

    <div class="section-head"><svg width="11" height="8" style="color:var(--ink)"><use href="#truck"/></svg>LIEFERADRESSE</div>
    <div class="row"><div><div class="t">KEINE LIEFERADRESSE ANGEGEBEN</div><div class="s">Bitte angeben</div></div><span class="go"><svg width="8" height="8"><use href="#chev"/></svg></span></div>

    <div class="section-head"><svg width="11" height="8" style="color:var(--ink)"><use href="#card"/></svg>ZAHLUNGSART</div>
    <div class="row"><div><div class="t">KEINE ZAHLUNGSART ANGEGEBEN</div></div><span class="go"><svg width="8" height="8"><use href="#chev"/></svg></span></div>

    <div class="section-head"><svg width="9" height="10" viewBox="0 0 9 10"><path d="M4.5 0C2.5 0 1.5 1.5 1.5 3.5V6L0 8h9L7.5 6V3.5C7.5 1.5 6.5 0 4.5 0z" fill="#2b3340"/><circle cx="4.5" cy="9" r="1" fill="#2b3340"/></svg>PUSH NACHRICHTEN</div>
    <div class="row" style="border-bottom:none"><span class="toggle"></span><div><div class="t">BRAVIO (PIXA 5)</div><div class="s">Dieses Gerät</div></div></div>
  </div>

  <footer class="footbar">Copyright © 2017 All Rights Reserved<span class="ver">v0.1</span></footer>
</section>

</body>
</html>
```